We need a design for a clothing tag for our summer hats & sandals line. Tag should be 2.25" high by 2" wide with a little hole punch circle in the top center. The brand is "Coral Drift" so it should have that name on the tag & then I would also like "Summer Apparel" on the tag somewhere lower on the tag perhaps in a bit smaller font. It should obviously be summer themed- with a picture of a beach or sand- something to that effect. Our previous brand was "Lumen Days"- I have attached that artwork so you can get an idea of what we are looking for.

Logo Text

Coral Drift

```html
<!DOCTYPE html>
<html lang="en">
<head>
<meta charset="utf-8">
<title>Coral Drift – Summer Apparel Tag</title>
<link href="https://fonts.googleapis.com/css2?family=Ultra&family=Montserrat:wght@400&display=swap" rel="stylesheet">
<style>
  :root {
    --page-bg: #ffffff;
    --sky-deep: #3f62b5;
    --sky-mid: #5a84d3;
    --sky-light: #c9d6ef;
    --horizon: #2fb8cf;
    --water: #7fdce4;
    --shallows: #c8eef0;
    --sand: #ece9e1;
    --brand-text: #ffffff;
    --tagline-text: #111111;
    --punch-hole: #ffffff;
    --punch-edge: #b9c6e3;
  }
  html, body {
    margin: 0;
    padding: 0;
    width: 1200px;
    height: 1200px;
    overflow: hidden;
    background: var(--page-bg);
  }
  .canvas {
    position: relative;
    width: 1200px;
    height: 1200px;
  }
  .hang-tag {
    position: absolute;
    left: 419px;
    top: 402px;
    width: 352px;
    height: 352px;
    overflow: hidden;
  }
  .beach-scene {
    position: absolute;
    inset: 0;
    background:
      radial-gradient(ellipse 90% 55% at 95% 100%, var(--sand) 0%, var(--sand) 35%, rgba(236,233,225,0) 70%),
      linear-gradient(to bottom,
        var(--sky-light) 0%,
        var(--sky-mid) 30%,
        var(--sky-mid) 52%,
        var(--horizon) 54%,
        var(--water) 66%,
        var(--shallows) 85%,
        var(--sand) 100%);
  }
  .beach-scene::before {
    content: "";
    position: absolute;
    inset: 0;
    background: linear-gradient(225deg, var(--sky-deep) 0%, rgba(63,98,181,0) 40%);
  }
  .punch-hole {
    position: absolute;
    left: 50%;
    top: 14px;
    width: 18px;
    height: 18px;
    margin-left: -9px;
    border-radius: 50%;
    background: var(--punch-hole);
    box-shadow: inset 0 0 0 1px var(--punch-edge);
  }
  .brand-name {
    position: absolute;
    inset: 0;
    margin: 0;
    font-family: "Ultra", "Rockwell Extra Bold", "Georgia", serif;
    font-weight: 700;
    color: var(--brand-text);
    font-size: 70px;
    line-height: 1;
    letter-spacing: 0;
    text-transform: uppercase;
  }
  .brand-name .line-one {
    position: absolute;
    left: 28px;
    top: 92px;
    white-space: nowrap;
  }
  .brand-name .line-two {
    position: absolute;
    left: 68px;
    top: 150px;
    white-space: nowrap;
  }
  .tagline {
    position: absolute;
    left: 130px;
    top: 312px;
    margin: 0;
    font-family: "Montserrat", sans-serif;
    font-weight: 400;
    font-size: 18px;
    letter-spacing: 0.5px;
    color: var(--tagline-text);
    white-space: nowrap;
  }
</style>
</head>
<body>
  <div class="canvas">
    <div class="hang-tag">
      <div class="beach-scene" role="img" aria-label="Photo of a tropical beach: blue sky with wispy clouds, turquoise shallow sea with small boats on the horizon, white sand shore"></div>
      <div class="punch-hole"></div>
      <h1 class="brand-name">
        <span class="line-one">Coral</span>
        <span class="line-two">Drift</span>
      </h1>
      <p class="tagline">SUMMER APPAREL</p>
    </div>
  </div>
</body>
</html>
```